Business card design for Tolbrin Waste

I would like double-sided business cards for myself and my partner that includes our logo and the existing colour scheme. We provide waste and environmental services to customers in the motor-vehicle and engineering industries.

```html
<!DOCTYPE html>
<html lang="en">
<head>
<meta charset="utf-8">
<title>Tolbrin Waste – Business Card</title>
<link href="https://fonts.googleapis.com/css2?family=Roboto:wght@400;500;700&display=swap" rel="stylesheet">
<style>
  :root {
    --green-dark: #5fa532;
    --green-mid: #7dbb34;
    --green-light: #9ccf3a;
    --ink: #3b3f44;
    --ink-soft: #5c6166;
    --paper: #ffffff;
    --backdrop: #eceee9;
  }
  * { box-sizing: border-box; margin: 0; padding: 0; }
  html, body {
    width: 1200px; height: 800px; overflow: hidden;
    background: var(--backdrop);
    font-family: "Roboto", Arial, sans-serif;
  }
  .canvas {
    position: relative; width: 1200px; height: 800px;
    display: flex; align-items: center; justify-content: center; gap: 60px;
  }
  .card {
    position: relative; width: 520px; height: 300px; overflow: hidden;
    border-radius: 4px;
    box-shadow: 0 10px 28px rgba(0,0,0,0.14);
  }

  /* Front */
  .card-front {
    background: radial-gradient(ellipse at 40% 70%, var(--green-light) 0%, var(--green-mid) 45%, var(--green-dark) 100%);
    display: flex; align-items: center; justify-content: center;
  }
  .brand {
    display: flex; align-items: center; gap: 14px;
  }
  .brand-dot {
    width: 44px; height: 44px; border-radius: 50%;
    border: 3px solid var(--paper);
  }
  .brand-name {
    font-weight: 700; font-size: 34px; letter-spacing: 1px;
    color: var(--paper); text-transform: uppercase;
  }

  /* Back */
  .card-back { background: var(--paper); }
  .back-band { position: absolute; inset: 0; width: 100%; height: 100%; }
  .back-content {
    position: absolute; left: 200px; top: 34px; right: 24px;
  }
  .card-back .brand { gap: 10px; margin-bottom: 18px; }
  .card-back .brand-dot {
    width: 36px; height: 36px; border: 3px solid var(--green-mid);
  }
  .card-back .brand-name { font-size: 24px; color: var(--ink); }
  .person-name {
    font-weight: 500; font-size: 17px; color: var(--green-mid);
  }
  .person-role {
    font-size: 11px; color: var(--ink-soft); margin-bottom: 16px;
  }
  .contact-list { list-style: none; }
  .contact-item {
    display: flex; align-items: flex-start; gap: 10px;
    font-size: 12.5px; color: var(--ink); margin-bottom: 9px; line-height: 1.25;
  }
  .contact-icon {
    flex: none; width: 16px; height: 16px; border-radius: 50%;
    background: var(--green-mid);
    display: flex; align-items: center; justify-content: center;
  }
  .contact-icon svg { width: 10px; height: 10px; }
</style>
</head>
<body>
<main class="canvas">

  <section class="card card-front" aria-label="Card front">
    <div class="brand">
      <span class="brand-dot"></span>
      <span class="brand-name">Tolbrin Waste</span>
    </div>
  </section>

  <section class="card card-back" aria-label="Card back">
    <svg class="back-band" viewBox="0 0 520 300" preserveAspectRatio="none" aria-hidden="true">
      <defs>
        <linearGradient id="bandGradient" x1="0" y1="0" x2="0.3" y2="1">
          <stop offset="0" stop-color="#5fa532"/>
          <stop offset="1" stop-color="#8ec63a"/>
        </linearGradient>
      </defs>
      <path d="M0 0 H178 C120 40 88 110 100 190 C106 240 130 280 150 300 H0 Z" fill="url(#bandGradient)"/>
      <path d="M178 0 C128 44 100 112 112 190 C118 236 140 276 158 300 H150 C130 280 106 240 100 190 C88 110 120 40 178 0 Z" fill="#9ccf3a"/>
      <path d="M188 0 C136 46 110 114 122 190 C128 236 148 276 166 300 H158 C140 276 118 236 112 190 C100 112 128 44 178 0 Z" fill="#ffffff"/>
      <path d="M196 0 C144 48 120 116 132 190 C138 234 156 274 172 300 H166 C148 276 128 236 122 190 C110 114 136 46 188 0 Z" fill="#7dbb34"/>
    </svg>

    <div class="back-content">
      <div class="brand">
        <span class="brand-dot"></span>
        <span class="brand-name">Tolbrin Waste</span>
      </div>
      <p class="person-name">Maren Holloway</p>
      <p class="person-role">Manager</p>
      <ul class="contact-list">
        <li class="contact-item">
          <span class="contact-icon"><svg viewBox="0 0 10 10"><path d="M2 1 L4 1 L4.6 3 L3.5 3.8 C4 5 5 6 6.2 6.5 L7 5.4 L9 6 L9 8 C5 8.5 1.5 5 2 1 Z" fill="#fff"/></svg></span>
          0871 26 38 14
        </li>
        <li class="contact-item">
          <span class="contact-icon"><svg viewBox="0 0 10 10"><rect x="1" y="2.5" width="8" height="5" fill="#fff"/><path d="M1 2.5 L5 5.5 L9 2.5" stroke="#7dbb34" stroke-width="0.8" fill="none"/></svg></span>
          info@tolbrinwaste.com
        </li>
        <li class="contact-item">
          <span class="contact-icon"><svg viewBox="0 0 10 10"><circle cx="5" cy="5" r="3.8" stroke="#fff" stroke-width="0.9" fill="none"/><ellipse cx="5" cy="5" rx="1.6" ry="3.8" stroke="#fff" stroke-width="0.8" fill="none"/><path d="M1.2 5 H8.8" stroke="#fff" stroke-width="0.8"/></svg></span>
          www.tolbrinwaste.com
        </li>
        <li class="contact-item">
          <span class="contact-icon"><svg viewBox="0 0 10 10"><path d="M5 9.2 C3 6.6 2 5.2 2 3.8 A3 3 0 0 1 8 3.8 C8 5.2 7 6.6 5 9.2 Z" fill="#fff"/><circle cx="5" cy="3.8" r="1.1" fill="#7dbb34"/></svg></span>
          <span>No. 21870, quarry lane<br>fairview 412</span>
        </li>
      </ul>
    </div>
  </section>

</main>
</body>
</html>
```